Satin Decor Paint Label

We will have three different sizes for this label but the dimensions for the medium size are 2" tall by 11.75'' wide. Please work off that.

Our colors are typically black and white but feel free to incorporate silver, gold, bronze or any combination. We would like to see multiple color variations of your designs.

General Info needed on label:
2947
Coatings
Interior Decor Paint
Furniture, Trim, Cabinets
Acrylic Waterborne Urethane
Satin Finish
16 FL. OZ. - 473 mL
````````````````````````````````````````````````````````````````````````````````````````````
Your design does not have to be the same as the one in the attached image.

You can put Satin Finish or Interior Decor Paint or something else going vertically up the side.

The label will be on a container like the the one in the attached image. Please have your design work on the same container.

```html
<!DOCTYPE html>
<html lang="en">
<head>
<meta charset="utf-8">
<title>2947 Coatings – Satin Finish Label</title>
<link href="https://fonts.googleapis.com/css2?family=Montserrat:wght@500;600;700;800&display=swap" rel="stylesheet">
<style>
  :root {
    --ink: #0b0b0b;
    --stage: #0a0a0a;
    --silver-light: #f7f7f7;
    --silver-mid: #e4e4e4;
    --silver-dark: #d2d2d2;
    --gold: #c9a464;
    --paper: #ffffff;
  }
  * { margin: 0; padding: 0; box-sizing: border-box; }
  html, body {
    width: 977px; height: 1200px; overflow: hidden;
    background: var(--stage);
    font-family: "Montserrat", Arial, sans-serif;
    color: var(--ink);
  }
  .label {
    position: absolute; left: 25px; top: 388px;
    width: 926px; height: 424px;
    background: linear-gradient(90deg,
      var(--silver-mid) 0%, var(--silver-light) 18%, var(--paper) 38%,
      var(--silver-light) 62%, var(--silver-mid) 82%, var(--silver-dark) 100%);
  }
  .brand-name {
    position: absolute; left: 262px; width: 404px; top: 112px;
    text-align: center; font-weight: 700; font-size: 44px;
    line-height: 1; letter-spacing: 0; white-space: nowrap;
    color: var(--ink);
  }
  .uses {
    position: absolute; left: 262px; width: 404px; top: 262px;
    display: flex; justify-content: space-between; align-items: center;
    font-weight: 700; font-size: 17px; letter-spacing: 0.2px;
  }
  .uses span { padding: 8px 0 6px; }
  .uses .divider { width: 2px; background: var(--gold); padding: 0; height: 34px; }
  .base-type {
    position: absolute; left: 262px; width: 404px; top: 305px; height: 31px;
    background: var(--ink); color: var(--paper);
    font-weight: 500; font-size: 16.5px; letter-spacing: 0.6px;
    display: flex; align-items: center; justify-content: center;
  }
  .finish {
    position: absolute; left: 262px; width: 404px; top: 340px;
    text-align: center; font-weight: 800; font-size: 34px; letter-spacing: 0.5px;
  }
  .volume {
    position: absolute; left: 262px; width: 404px; top: 384px;
    text-align: center; font-weight: 500; font-size: 16px;
  }
  .side-title {
    position: absolute; left: 697px; top: 155px;
    width: 305px; height: 56px;
    transform: rotate(-90deg);
    display: flex; align-items: center; justify-content: space-between;
  }
  .side-title .kind {
    font-weight: 600; font-size: 24px; line-height: 0.98; letter-spacing: 0.2px;
  }
  .side-title .product { font-weight: 800; font-size: 64px; line-height: 1; letter-spacing: -1px; }
</style>
</head>
<body>
  <section class="label">
    <h1 class="brand-name">2947 COATINGS</h1>
    <div class="uses">
      <span>FURNITURE</span><span class="divider"></span>
      <span>TRIM</span><span class="divider"></span>
      <span>CABINETS</span>
    </div>
    <div class="base-type">ACRYLIC WATERBORNE URETHANE</div>
    <div class="finish">SATIN FINISH</div>
    <div class="volume">16 FL.OZ. / 473 ML</div>
    <div class="side-title">
      <div class="kind">INTERIOR<br>DECOR</div>
      <div class="product">Paint</div>
    </div>
  </section>
</body>
</html>
```